Meadowlark Soaps Business Card

The new business card design will incorporate my new logo components designed by one of your designers. Meadowlark Soaps creates high quality soaps and bath products. They would be suited for a Spa, Bed and Breakfast, Boutique environment. The look should be a white background.
Classy, soft and using the colour palet of the logo. The card will be two sided.

Reason: Need more time to make some changes and decide.

Target Market(s)

Looking to appeal to an upper end market. Spas, boutiques, independent gift stores, bridal salons, bed and breakfast, etc. I want the card to impart a sense of elegance, tranquility and Meadowlark. But also quality and value.

Industry/Entity Type

Business

Font styles to use
Sans Serif
Script

Requirements
Must have
• My logo on the front. But also on the back but faded out to allow written notes on the back.
On the front : Marta Quennell
Owner/Creator
47 Ashcombe Rd
Guelph, Ont K7R 2M5
555.014.2938
Creating Quality Handcrafted Soaps And Bath Products
Custom and Wholesale Orders Welcome
Www.meadowlarksoaps.ca
Www.facebook.com / MeadowlarkSoapandBath
info@meadowlarksoaps.ca

```html
<!DOCTYPE html>
<html lang="en">
<head>
<meta charset="utf-8">
<title>Meadowlark Soaps Business Card</title>
<link href="https://fonts.googleapis.com/css2?family=Mulish:wght@400;700&display=swap" rel="stylesheet">
<style>
  :root {
    --page: #2b2d30;
    --card: #ffffff;
    --teal: #74a99d;
    --teal-deep: #5f968a;
    --teal-soft: #d6ebe5;
    --teal-faint: #eef6f3;
    --sand: #e7d3bf;
    --stone: #c9c9c6;
    --text: #6d9a90;
  }
  * { box-sizing: border-box; margin: 0; padding: 0; }
  html, body { width: 1200px; height: 790px; overflow: hidden; }
  body {
    background: var(--page);
    font-family: "Mulish", sans-serif;
    color: var(--text);
    position: relative;
  }
  .card {
    position: absolute;
    width: 560px;
    height: 320px;
    background: var(--card);
    box-shadow: 0 6px 18px rgba(0,0,0,.35);
    overflow: hidden;
  }

  /* Back side */
  .card-back { left: 40px; top: 70px; }
  .card-back .texture {
    position: absolute; inset: 0;
    background:
      radial-gradient(ellipse at 30% 40%, rgba(201,201,198,.22), transparent 60%),
      radial-gradient(ellipse at 75% 30%, rgba(231,211,191,.18), transparent 55%),
      radial-gradient(ellipse at 60% 80%, rgba(116,169,157,.10), transparent 60%);
  }
  .card-back .logo-art {
    position: absolute; left: 62px; top: 90px; width: 140px; height: 150px;
    border-radius: 50% 50% 30% 30%;
    background: radial-gradient(ellipse at 50% 40%, rgba(116,169,157,.45), rgba(231,211,191,.25) 60%, transparent 75%);
  }
  .card-back .wordmark {
    position: absolute; left: 40px; top: 238px; width: 240px; text-align: center;
    color: rgba(116,169,157,.7);
  }

  /* Front side */
  .card-front { left: 600px; top: 400px; }
  .card-front .logo-art {
    position: absolute; left: 70px; top: 40px; width: 190px; height: 160px;
    border-radius: 50% 50% 35% 35%;
    background: radial-gradient(ellipse at 50% 40%, rgba(116,169,157,.6), rgba(231,211,191,.4) 60%, transparent 76%);
  }
  .card-front .wordmark {
    position: absolute; left: 40px; top: 196px; width: 260px; text-align: center;
    color: var(--teal);
  }
  .wordmark .name { display: block; font-size: 34px; font-weight: 400; letter-spacing: .5px; line-height: 1; }
  .wordmark .sub { display: block; font-size: 12px; font-weight: 400; letter-spacing: 5px; margin-top: 6px; }
  .card-back .wordmark .name { font-size: 30px; }

  .contact {
    position: absolute; left: 330px; top: 26px; font-size: 14px; line-height: 1.35;
  }
  .contact .person { font-size: 19px; font-weight: 700; color: var(--teal-deep); }
  .contact .role { margin-bottom: 14px; }
  .contact .address { margin-bottom: 8px; }
  .contact ul { list-style: none; }
  .contact li { display: flex; align-items: center; gap: 7px; }
  .contact li svg { width: 12px; height: 12px; flex: none; fill: var(--teal-deep); }

  .band {
    position: absolute; left: 0; right: 0; bottom: 0; height: 80px;
    background: linear-gradient(180deg, var(--teal-faint), var(--teal-soft));
  }
  .band .speckle {
    position: absolute; right: 0; top: -40px; width: 240px; height: 120px;
    background: radial-gradient(ellipse at 60% 50%, rgba(231,211,191,.55), rgba(116,169,157,.25) 55%, transparent 75%);
  }
  .tagline {
    position: absolute; left: 24px; bottom: 16px; font-size: 15px; line-height: 1.35; color: var(--teal-deep);
  }
</style>
</head>
<body>

<section class="card card-back" aria-label="Card back">
  <div class="texture" role="img" aria-label="Faint scattered soft paint dabs across the card"></div>
  <div class="logo-art" role="img" aria-label="Faded logo symbol area"></div>
  <div class="wordmark">
    <span class="name">Meadowlark</span>
    <span class="sub">SOAPS</span>
  </div>
</section>

<section class="card card-front" aria-label="Card front">
  <div class="logo-art" role="img" aria-label="Logo symbol area in teal and sand tones"></div>
  <div class="wordmark">
    <span class="name">Meadowlark</span>
    <span class="sub">SOAPS</span>
  </div>

  <div class="contact">
    <div class="person">Marta Quennell</div>
    <div class="role">Owner/Creator</div>
    <div class="address">47 Ashcombe Rd<br>Guelph, Ont K7R 2M5</div>
    <ul>
      <li><svg viewBox="0 0 12 12"><path d="M2 1h2l1 3-1.3 1a6 6 0 0 0 3.3 3.3L8 7l3 1v2a1 1 0 0 1-1 1A9 9 0 0 1 1 2a1 1 0 0 1 1-1z"/></svg>555.014.2938</li>
      <li><svg viewBox="0 0 12 12"><path d="M1 2h10v8H1z M1 2l5 4 5-4" fill="none" stroke="currentColor" stroke-width="1.2" style="stroke:#5f968a"/></svg>info@meadowlarksoaps.ca</li>
      <li><svg viewBox="0 0 12 12"><circle cx="6" cy="6" r="5" fill="none" stroke="#5f968a" stroke-width="1.2"/><path d="M1 6h10M6 1c2 2.5 2 7.5 0 10M6 1c-2 2.5-2 7.5 0 10" fill="none" stroke="#5f968a" stroke-width="1"/></svg>www.meadowlarksoaps.ca</li>
      <li><svg viewBox="0 0 12 12"><circle cx="6" cy="6" r="5"/></svg>MeadowlarkSoapandBath</li>
    </ul>
  </div>

  <div class="band">
    <div class="speckle" role="img" aria-label="Scattered soft paint dabs in teal and sand"></div>
    <p class="tagline">Creating Quality Handcrafted Soaps And Bath Products<br>Custom and Wholesale Orders Welcome</p>
  </div>
</section>

</body>
</html>
```